Australian tool shop needs a label designed for a new product

we need a label designed for a new product (Corvel Plus) but since its new to the market we want the label to be based on the design of the top 2 existing brands so it is instantly familiar with the customer, attached a photo of the 2 different brands that it needs to look like

Target Market(s)

BRICKLAYERS/ BUILDERS

Industry/Entity Type

Building Product

Requirements
Must have
• MUST HAVE SIMULAR FEELS AS THE UPLOADED IMAGE AND FEEL FAMILIAR WITH THOSE BRANDS

```html
<!DOCTYPE html>
<html lang="en">
<head>
<meta charset="utf-8">
<title>Hydrated Lime – Corvel Plus 20 kg Bag Label</title>
<link rel="stylesheet" href="https://fonts.googleapis.com/css2?family=Anton&family=Roboto+Condensed:wght@400;700&display=swap">
<style>
  :root {
    --navy: #00146e;
    --orange: #ff5a28;
    --white: #ffffff;
    --grey: #a6a6a6;
    --hatch: #8e94c4;
  }
  * { margin: 0; padding: 0; box-sizing: border-box; }
  html, body { width: 800px; height: 1200px; overflow: hidden; background: var(--white); }
  .label {
    position: relative;
    width: 800px;
    height: 1200px;
    overflow: hidden;
    background: var(--white);
    font-family: "Roboto Condensed", "Arial Narrow", sans-serif;
    color: var(--navy);
  }
  .label__backdrop { position: absolute; inset: 0; width: 800px; height: 1200px; }

  .weight-badge {
    position: absolute; left: 643px; top: 0; width: 122px; height: 97px;
  }
  .weight-badge__text {
    position: absolute; left: 0; right: 0; top: 14px;
    text-align: center; color: var(--white);
    font-family: "Anton", "Impact", sans-serif;
  }
  .weight-badge__value { font-size: 50px; line-height: 1; }
  .weight-badge__unit { font-size: 22px; margin-left: 2px; }

  .product-name {
    position: absolute; left: 84px; top: 172px;
    font-family: "Anton", "Impact", sans-serif;
    font-weight: 400; color: var(--orange);
    font-size: 124px; line-height: 115px; letter-spacing: 0;
    text-transform: uppercase;
  }

  .benefits {
    position: absolute; left: 82px; top: 450px;
    list-style: none; font-weight: 700;
    font-size: 24px; line-height: 28px; color: var(--navy);
  }

  .tool-artwork {
    position: absolute; left: 523px; top: 320px; width: 234px; height: 587px;
    border-radius: 117px 117px 60px 60px;
    background: linear-gradient(180deg, var(--grey) 0%, var(--grey) 50%, #e6e6e6 75%, var(--white) 100%);
  }

  .brand-name {
    position: absolute; left: 66px; top: 915px;
    font-weight: 700; font-size: 66px; line-height: 1;
    color: var(--white); letter-spacing: 1px;
  }

  .uses {
    position: absolute; left: 588px; top: 1012px; width: 190px;
    text-align: center; color: var(--white); font-weight: 700;
  }
  .uses__icons { display: flex; justify-content: space-between; padding: 0 2px; }
  .use { width: 88px; display: flex; flex-direction: column; align-items: center; }
  .use__icon { width: 77px; height: 77px; border-radius: 50%; background: var(--orange); }
  .use__label { margin-top: 6px; font-size: 15px; line-height: 18px; }
  .uses__more { margin-top: 14px; font-size: 15px; line-height: 17px; }

  .safety {
    position: absolute; left: 40px; top: 1097px; width: 400px; color: var(--white);
  }
  .safety__instructions {
    font-size: 16px; font-weight: 700; line-height: 20px;
    padding-bottom: 4px; border-bottom: 1.5px solid var(--white);
    width: 367px;
  }
  .safety__warning { margin-top: 7px; font-size: 17px; font-weight: 700; line-height: 20px; }
  .safety__detail { margin-top: 3px; font-size: 11px; font-weight: 400; line-height: 14px; }
</style>
</head>
<body>
<main class="label">
  <svg class="label__backdrop" viewBox="0 0 800 1200" aria-hidden="true">
    <polygon class="hatch-band" points="0,0 428,0 365,62 0,62" fill="var(--hatch)"/>
    <path class="navy-swoosh-line" d="M0 666 C 200 722, 460 748, 800 696" fill="none" stroke="var(--navy)" stroke-width="3"/>
    <path class="orange-band" d="M0 739 C 250 772, 500 770, 800 741 L800 800 C 560 828, 260 852, 0 824 Z" fill="var(--orange)"/>
    <path class="navy-base" d="M0 824 C 260 852, 560 828, 800 800 L800 1200 L0 1200 Z" fill="var(--navy)"/>
  </svg>

  <div class="weight-badge">
    <svg viewBox="0 0 122 97" width="122" height="97" aria-hidden="true">
      <path d="M0 0 H122 V70 Q122 76 116 79 L66 96 Q61 98 56 96 L6 79 Q0 76 0 70 Z" fill="var(--navy)"/>
    </svg>
    <div class="weight-badge__text"><span class="weight-badge__value">20</span><span class="weight-badge__unit">kg</span></div>
  </div>

  <h1 class="product-name">Hydrated<br>Lime</h1>

  <ul class="benefits">
    <li>Blends with sand &amp; cement for mortar</li>
    <li>Enhances mortar bond strength &amp; workability</li>
  </ul>

  <div class="tool-artwork" role="img" aria-label="Illustration of a bricklayer's trowel with navy and orange handle"></div>

  <p class="brand-name">Corvel Plus</p>

  <section class="uses">
    <div class="uses__icons">
      <div class="use">
        <div class="use__icon" role="img" aria-label="Mortar icon: trowel on a brick"></div>
        <span class="use__label">Mortar</span>
      </div>
      <div class="use">
        <div class="use__icon" role="img" aria-label="Gardening icon: fence and shrubs"></div>
        <span class="use__label">Gardening</span>
      </div>
    </div>
    <p class="uses__more">Plus Water treatment,<br>sanitising &amp; many other uses</p>
  </section>

  <section class="safety">
    <p class="safety__instructions">See Over For Instructions</p>
    <p class="safety__warning">Warning : Hazardous</p>
    <p class="safety__detail">Lorem ipsum dolor sit amet, consectetuer adipiscing elit, sed diam nonummy nibh euis-<br>mod tincidunt ut laoreet dolore magna aliquam erat volutpat. Ut wisi enim ad</p>
  </section>
</main>
</body>
</html>
```